Pelican Litigation Funding Letterhead & Document Template

We need a letter head designed for our fund. Our fund works with law firms and investors across the globe. We need a a cover letter template as well as a document template for subsequent pages. Blue and white color scheme is preferred. This is our predecessor's website: https://www.pelicanvq.com/index.html. Please see our logo attached. The logo color code is #19478d. Font is Gotham-Medium.
Target Market(s)
Sophisticated investors and law firms
Font styles to use
Sans Serif
Colors
0255a3

```html
<!DOCTYPE html>
<html lang="en">
<head>
<meta charset="utf-8">
<title>Pelican Litigation Funding Letterhead</title>
<link href="https://fonts.googleapis.com/css2?family=Montserrat:wght@500&family=Arimo:wght@400&display=swap" rel="stylesheet">
<style>
  :root {
    --brand-blue: #19478d;
    --band-blue: #17468a;
    --back-sheet: #1d4a92;
    --backdrop: #e2e2e2;
    --ink: #4a4a4a;
    --ink-soft: #555555;
    --paper-top: #ffffff;
    --paper-bottom: #ececec;
    --stripe: #f3f3f3;
    --signature-tone: #d9d9dd;
  }
  * { margin: 0; padding: 0; box-sizing: border-box; }
  html, body {
    width: 1200px;
    height: 1141px;
    overflow: hidden;
    background: linear-gradient(90deg, #dedede, #e8e8e8);
    position: relative;
  }
  .back-sheet {
    position: absolute;
    left: 312px;
    top: 59px;
    width: 675px;
    height: 948px;
    background: linear-gradient(135deg, #1f4f99, var(--back-sheet) 60%, #1a4489);
    box-shadow: 0 2px 6px rgba(0,0,0,0.25);
  }
  .letterhead {
    position: absolute;
    left: 249px;
    top: 117px;
    width: 674px;
    height: 948px;
    background: linear-gradient(160deg, var(--paper-top) 35%, var(--paper-bottom) 100%);
    box-shadow: 0 2px 6px rgba(0,0,0,0.3);
    font-family: "Arimo", Arial, sans-serif;
    color: var(--ink);
  }
  .brand-name {
    position: absolute;
    top: 107px;
    left: 0;
    width: 100%;
    text-align: center;
    font-family: "Montserrat", Arial, sans-serif;
    font-weight: 500;
    font-size: 13px;
    letter-spacing: 0.3px;
    color: var(--brand-blue);
    text-transform: uppercase;
  }
  .salutation {
    position: absolute;
    top: 236px;
    left: 50px;
    font-size: 17px;
    font-weight: 400;
    color: var(--ink-soft);
  }
  .letter-body {
    position: absolute;
    top: 285px;
    left: 50px;
    right: 50px;
    font-size: 9.6px;
    line-height: 14.4px;
    text-align: justify;
  }
  .letter-body p { margin-bottom: 14.4px; }
  .closing {
    position: absolute;
    top: 602px;
    left: 50px;
    font-size: 9.6px;
  }
  .signature {
    position: absolute;
    top: 636px;
    left: 46px;
    width: 195px;
    height: 54px;
    background: linear-gradient(90deg, var(--signature-tone), rgba(217,217,221,0.3));
    border-radius: 4px;
  }
  .contact-band {
    position: absolute;
    left: 0;
    bottom: 0;
    width: 100%;
    height: 57px;
    background: var(--band-blue);
    color: #ffffff;
    font-family: "Montserrat", Arial, sans-serif;
    font-weight: 500;
    font-size: 10.5px;
  }
  .band-stripe {
    position: absolute;
    left: 0;
    top: 0;
    width: 674px;
    height: 57px;
  }
  .contact-line {
    position: absolute;
    left: 0;
    width: 100%;
    padding-left: 142px;
    text-align: center;
    white-space: nowrap;
    line-height: 13px;
  }
  .contact-line.address { top: 14px; }
  .contact-line.channels { top: 28px; }
  .contact-item { display: inline-flex; align-items: center; gap: 3px; margin: 0 2px; }
  .contact-item svg { width: 9px; height: 9px; fill: #ffffff; }
</style>
</head>
<body>
  <div class="back-sheet" role="img" aria-label="Second page with an all-over blue geometric pattern"></div>

  <main class="letterhead">
    <div class="brand-name">Pelican Litigation Funding</div>

    <h1 class="salutation">Dear Mr. Carter,</h1>

    <section class="letter-body">
      <p>Lorem ipsum dolor sit amet, consectetur adipiscing elit. Donec orci purus, luctus vitae dignissim eu, iaculis sed purus. Vivamus faucibus, ipsum nec aliquet viverra, leo mauris condimentum ligula, sit amet sagittis enim ligula quis arcu. Nam egestas tortor id nisi porttitor mattis. In tortor ante, ultricies in suscipit a, tempus non massa. Vivamus et auctor mi. Fusce vel massa nulla. Phasellus nec eros mauris, et scelerisque orci.</p>
      <p>Donec malesuada orci vitae nulla accumsan porta a id massa. Quisque accumsan iaculis magna sit amet fringilla. Maecenas consequat, magna eget tincidunt semper, odio nibh rutrum mi, id feugiat ante nisi eu risus. Vestibulum nunc orci, rhoncus a placerat in, ultricies in mi. Cras mattis varius eros, vel fringilla nisi suscipit eget. Quisque scelerisque sagittis nulla at porttitor.</p>
      <p>Sed id augue vitae urna euismod commodo aliquet a quam. Pellentesque arcu velit, cursus et malesuada ut, consequat et diam. Nullam erat sem, rhoncus id ullamcorper vitae, rhoncus et arcu. In ultricies ultricies nulla, ut rutrum nisi iaculis at. Donec eu magna a metus ornare faucibus. Fusce aliquet faucibus ultricies. Morbi semper, est id tincidunt gravida, sem arcu adipiscing lacus, ac bibendum nulla leo eu purus. Quisque nec diam sed risus consectetur a ccumsan quis quis nibh. Vestibulum id purus lorem.</p>
      <p>It is a long established fact that a reader will be distracted by the readable content of a page when looking at its layout. The point of using Lorem Ipsum is that it has a more-or-less normal distribution of letters, as opposed to using ‘Content here, content here’, making it look like readable English. Many desktop publishing packages</p>
      <p>ada ut, consequat et diam. Nullam erat sem, rhoncus id ullamcorper vitae, rhoncus et arcu. In ultricies ultricies nulla, ut rutrum nisi iaculis at. Donec eu magna a metus ornare faucibus. Fusce aliquet faucibus ultricies. Morbi semper,</p>
    </section>

    <p class="closing">Sincerely,</p>
    <div class="signature" role="img" aria-label="Handwritten signature of the sender"></div>

    <footer class="contact-band">
      <svg class="band-stripe" viewBox="0 0 674 57" aria-hidden="true">
        <polygon points="116,0 169,0 131,57 78,57" fill="#f3f3f3"/>
      </svg>
      <div class="contact-line address">
        <span class="contact-item">
          <svg viewBox="0 0 10 10" aria-hidden="true"><path d="M5 0a3.5 3.5 0 0 0-3.5 3.5C1.5 6 5 10 5 10s3.5-4 3.5-6.5A3.5 3.5 0 0 0 5 0zm0 5a1.5 1.5 0 1 1 0-3 1.5 1.5 0 0 1 0 3z"/></svg>
          4120 Harbor View Road, Juneau, Alaska 99801
        </span>
      </div>
      <div class="contact-line channels">
        <span class="contact-item">
          <svg viewBox="0 0 10 10" aria-hidden="true"><path d="M2 0.5l1.8 2-1 1.2a6 6 0 0 0 3.5 3.5l1.2-1 2 1.8-1 1.7C4.5 9.5 0.5 5.5 0.3 1.5z"/></svg>
          555-148-3072
        </span>
        <span class="contact-item">
          <svg viewBox="0 0 10 10" aria-hidden="true"><path d="M0.5 2h9v6h-9z M0.5 2l4.5 3.5L9.5 2" fill="#ffffff" stroke="#17468a" stroke-width="0.8"/></svg>
          info@pelicanvq.com
        </span>
        <span class="contact-item">
          <svg viewBox="0 0 10 10" aria-hidden="true"><circle cx="5" cy="5" r="4.5"/><path d="M0.5 5h9M5 0.5c-2 2.5-2 6.5 0 9M5 0.5c2 2.5 2 6.5 0 9" stroke="#17468a" stroke-width="0.7" fill="none"/></svg>
          www.pelicanvq.com
        </span>
      </div>
    </footer>
  </main>
</body>
</html>
```